8x8 Social Media Ad - Harbor Summit Expo

Attention Real Estate Agents
Please join us for our
Quarterly Real Estate Training Expo
The 2nd Saturday of February, May, August and November
Our Next Training Expo is _________________________________
From 9 am to 1 pm
at
Marlowe Suites Fernridge Station
4187 Copperleaf Lane, Greenbelt, MD 20770
Scheduled Speakers
9:00 am - Desmond Pryce - Orientation
9:30 am - Terrell Oakes - Multiple Income Streams / Keystone Track
10:00 am - Lorna Beckett - Marketing though Social Media
10:45 am - Raul Denning - Generating Business through Kelp-Nest
11:30 am - Tunde Adesemi - Real Estate Investing
12:15 pm - Marcus Oyelowo - (Main Speaker) Training Topic TBA
For more information call Desmond Pryce at (240) 555-0192 or email dpryce@harborsummithomes.example

```html
<!DOCTYPE html>
<html lang="en">
<head>
<meta charset="utf-8">
<title>Harbor Summit Expo – Quarterly Real Estate Training Expo</title>
<link href="https://fonts.googleapis.com/css2?family=Barlow:wght@300;400;500;600;700&display=swap" rel="stylesheet">
<style>
:root{
  --teal:#0e94a0;
  --teal-dark:#0b7f8a;
  --black:#000;
  --white:#fff;
  --backdrop:#d1d2d4;
  --photo-a:#6f7d86;
  --photo-b:#c9cfd3;
}
*{margin:0;padding:0;box-sizing:border-box}
html,body{width:1200px;height:1010px;overflow:hidden;background:var(--backdrop)}
body{font-family:"Barlow",Arial,sans-serif;position:relative}
.ad{position:absolute;left:199px;top:105px;width:802px;height:802px;background:var(--white);overflow:hidden}
.ad > *{position:absolute}
.shapes{left:0;top:0;width:802px;height:802px}
.brand{left:30px;top:70px;display:flex;align-items:center;gap:10px;color:var(--black);font-weight:700;font-size:19px;line-height:1.15;letter-spacing:.3px}
.brand-mark{width:30px;height:30px;background:var(--teal)}
.kicker{left:352px;top:30px;color:var(--teal);font-weight:700;font-size:25px;letter-spacing:.6px}
.headline{left:352px;top:66px;color:var(--white);font-size:27px;line-height:1.2;letter-spacing:.5px}
.headline .light{font-weight:300;display:block}
.headline strong{display:block;font-weight:700;font-size:32px;line-height:1.1;letter-spacing:.8px}
.dates{left:0;top:190px;width:802px;text-align:center;color:var(--white);font-size:20px;font-weight:500;line-height:24px;letter-spacing:.4px}
.venue{left:0;top:254px;width:802px;text-align:center;color:var(--white);font-size:19.5px;line-height:24px;letter-spacing:.4px}
.venue b{font-weight:700}
.section-title{left:0;top:325px;width:802px;text-align:center;color:var(--white);font-weight:700;font-size:18px;letter-spacing:.8px}
.photo{border-radius:50%;border:4px solid var(--white);background:linear-gradient(160deg,var(--photo-b),var(--photo-a));box-shadow:0 2px 5px rgba(0,0,0,.35)}
.photo.main{border:5px solid var(--teal);box-shadow:none}
.time{color:var(--white);font-weight:700;font-size:17px}
.talk{color:var(--teal);font-size:14.5px;line-height:16px;font-weight:500}
.talk b{display:block;font-size:16.5px;font-weight:700;line-height:20px}
.keynote{left:619px;top:586px;color:var(--teal);line-height:21px}
.keynote .ktime,.keynote .kname{font-weight:700;font-size:20px}
.keynote .krole{font-weight:500;font-size:18px}
.keynote .ktopic{font-weight:300;font-size:17px}
.contact{left:0;top:726px;width:802px;text-align:center;color:var(--white);font-size:21px;line-height:26px;letter-spacing:.2px}
.contact b{font-weight:700}
</style>
</head>
<body>
<main class="ad">
  <svg class="shapes" viewBox="0 0 802 802" aria-hidden="true">
    <polygon points="291,0 802,0 802,23 285,23" fill="var(--teal)"/>
    <polygon points="272,58 802,58 802,180 248,180" fill="var(--teal)"/>
    <rect x="0" y="186" width="802" height="61" fill="var(--black)"/>
    <rect x="0" y="251" width="802" height="54" fill="var(--teal)"/>
    <rect x="0" y="310" width="802" height="400" fill="var(--teal)"/>
    <line x1="0" y1="336" x2="282" y2="336" stroke="var(--white)" stroke-width="1.5"/>
    <line x1="518" y1="336" x2="802" y2="336" stroke="var(--white)" stroke-width="1.5"/>
    <circle cx="811" cy="575" r="265" fill="var(--white)"/>
    <rect x="70" y="403" width="520" height="2" fill="var(--white)"/>
    <rect x="70" y="407" width="200" height="55" fill="var(--white)"/>
    <rect x="320" y="407" width="268" height="55" fill="var(--white)"/>
    <rect x="70" y="506" width="520" height="2" fill="var(--white)"/>
    <rect x="70" y="510" width="200" height="56" fill="var(--white)"/>
    <rect x="320" y="510" width="268" height="56" fill="var(--white)"/>
    <rect x="70" y="624" width="520" height="2" fill="var(--white)"/>
    <rect x="70" y="628" width="520" height="42" fill="var(--white)"/>
    <rect x="0" y="710" width="802" height="92" fill="var(--black)"/>
  </svg>

  <div class="brand"><span class="brand-mark"></span><span>HARBOR SUMMIT<br>REALTY GROUP</span></div>

  <p class="kicker">ATTENTION REAL ESTATE AGENTS</p>
  <h1 class="headline"><span class="light">PLEASE JOIN US FOR OUR</span><strong>QUARTERLY REAL ESTATE<br>TRAINING EXPO</strong></h1>

  <p class="dates">THE 2ND SATURDAY OF FEBRUARY, MAY, AUGUST AND NOVEMBER<br>OUR NEXT TRAINING EXPO IS.</p>
  <p class="venue"><b>FROM 9 AM TO 1 PM</b>&nbsp; AT MARLOWE SUITES FERNRIDGE STATION<br>4187 COPPERLEAF LANE, GREENBELT, MD 20770</p>

  <h2 class="section-title">SCHEDULED SPEAKERS</h2>

  <div class="photo" role="img" aria-label="Portrait of Desmond Pryce" style="left:16px;top:365px;width:104px;height:104px"></div>
  <span class="time" style="left:127px;top:373px">9:00 am</span>
  <p class="talk" style="left:127px;top:403px"><b>Desmond Pryce</b>Orientation</p>

  <div class="photo" role="img" aria-label="Portrait of Terrell Oakes" style="left:270px;top:365px;width:104px;height:104px"></div>
  <span class="time" style="left:389px;top:373px">9:30 am</span>
  <p class="talk" style="left:389px;top:403px"><b>Terrell Oakes</b>Multiple Income<br>Streams / Keystone Track</p>

  <div class="photo" role="img" aria-label="Portrait of Lorna Beckett" style="left:16px;top:477px;width:104px;height:104px"></div>
  <span class="time" style="left:127px;top:482px">10:00 am</span>
  <p class="talk" style="left:127px;top:512px"><b>Lorna Beckett</b>Marketing though<br>Social Media</p>

  <div class="photo" role="img" aria-label="Portrait of Raul Denning" style="left:270px;top:486px;width:104px;height:104px"></div>
  <span class="time" style="left:387px;top:482px">10:45 am</span>
  <p class="talk" style="left:387px;top:512px"><b>Raul Denning</b>Generating Business<br>through Kelp-Nest</p>

  <div class="photo" role="img" aria-label="Portrait of Tunde Adesemi" style="left:16px;top:588px;width:104px;height:104px"></div>
  <span class="time" style="left:133px;top:600px">11:30 am</span>
  <p class="talk" style="left:133px;top:630px"><b>Tunde Adesemi</b>Real Estate Investing</p>

  <div class="photo main" role="img" aria-label="Portrait of main speaker Marcus Oyelowo" style="left:565px;top:351px;width:228px;height:228px"></div>
  <div class="keynote">
    <div class="ktime">12:15 pm</div>
    <div class="kname">Marcus Oyelowo</div>
    <div class="krole">(Main Speaker)</div>
    <div class="ktopic">Training Topic TBA</div>
  </div>

  <p class="contact">For more information call<br>Desmond Pryce at <b>(240) 555-0192</b> or email <b>dpryce@harborsummithomes.example</b></p>
</main>
</body>
</html>
```